Verdant Loop Advisors, LLC

I am looking for a simple, clear layout with my logo prominent and embossed, on the best quality card stock available. I would like the business name and phone number included on the card as well......I dont want my name anywhere on the card and I would like my logo embossed on the card......something simple with a white back......open to designs as long as they go along with recycling symbols and green type stuff.....The address, website, cell number, fax number, and email are listed below

5374 Tillbury Fenwood Road
Marrowfield, MD 20999

c. 240.555.0143 f. 240.555.0187
e. sales@verdantloopadvisors.example
w. www.verdantloopadvisors.example

Industry/Entity Type

Recycling

```html
<!DOCTYPE html>
<html lang="en">
<head>
<meta charset="utf-8">
<title>Verdant Loop Advisors, LLC — Business Card</title>
<link rel="stylesheet" href="https://fonts.googleapis.com/css2?family=Orbitron:wght@600;800&display=swap">
<style>
  :root {
    --backdrop: #e9ece6;
    --lime-light: #c8ec5a;
    --lime: #9bd92a;
    --lime-deep: #6fbf1c;
    --band-white: #f6f7f3;
    --band-shade: #dfe2dc;
    --ink-dark: #2e3323;
    --mark-green: #1f7a35;
    --text-light: #eef8d4;
    --text-green: #2f7f2a;
  }
  * { margin: 0; padding: 0; box-sizing: border-box; }
  html, body {
    width: 1200px; height: 800px; overflow: hidden;
    background: var(--backdrop);
    font-family: "Orbitron", "Segoe UI", sans-serif;
  }
  .business-card {
    position: absolute; left: 75px; top: 100px;
    width: 1050px; height: 600px;
    border-radius: 6px; overflow: hidden;
    background: radial-gradient(ellipse at 70% 75%, var(--lime-light) 0%, var(--lime) 45%, var(--lime-deep) 100%);
    box-shadow: 0 18px 40px rgba(40, 50, 30, 0.25);
  }
  .card-texture {
    position: absolute; inset: 0;
    background: linear-gradient(160deg, rgba(255,255,255,0.18) 0%, rgba(255,255,255,0) 40%, rgba(255,255,255,0.12) 80%);
  }
  .name-band { position: absolute; left: 0; top: 90px; width: 1050px; height: 250px; }
  .website {
    position: absolute; right: 48px; top: 40px;
    font-size: 25px; font-weight: 600; letter-spacing: 1px;
    color: var(--text-light); text-transform: uppercase;
  }
  .identity {
    position: absolute; left: 70px; top: 150px;
    display: flex; align-items: center; gap: 28px;
  }
  .identity-dot {
    width: 90px; height: 90px; border-radius: 50%;
    background: var(--mark-green);
  }
  .company-name {
    color: var(--ink-dark); font-weight: 800; text-transform: uppercase; line-height: 1.05;
  }
  .company-name .primary { display: block; font-size: 62px; letter-spacing: 1px; }
  .company-name .secondary { display: block; font-size: 30px; letter-spacing: 8px; margin-top: 6px; }
  .phones {
    position: absolute; right: 48px; top: 345px; text-align: right;
    color: var(--text-light); font-weight: 800; line-height: 1.15;
  }
  .phones .cell { font-size: 44px; }
  .phones .fax { font-size: 36px; }
  .address {
    position: absolute; right: 48px; top: 465px; text-align: right;
    color: var(--text-light); font-weight: 600; font-size: 22px; font-style: normal;
    line-height: 1.3; text-transform: uppercase;
  }
  .email {
    position: absolute; left: 40px; bottom: 28px;
    color: var(--text-green); font-weight: 600; font-size: 22px; text-transform: uppercase;
  }
</style>
</head>
<body>
  <main class="business-card">
    <div class="card-texture" role="img" aria-label="Soft green background with faint recycling arrow shapes"></div>

    <svg class="name-band" viewBox="0 0 1050 250" preserveAspectRatio="none" aria-hidden="true">
      <path d="M0 70 C 180 40, 360 95, 560 55 S 900 20, 1050 0 L 1050 150 C 880 190, 700 150, 520 200 S 160 235, 0 250 Z" fill="var(--band-shade)"/>
      <path d="M0 80 C 180 50, 360 105, 560 65 S 900 30, 1050 10 L 1050 140 C 880 180, 700 140, 520 190 S 160 225, 0 240 Z" fill="var(--band-white)"/>
    </svg>

    <p class="website">www.verdantloopadvisors.example</p>

    <div class="identity">
      <span class="identity-dot" aria-hidden="true"></span>
      <h1 class="company-name">
        <span class="primary">Verdant Loop</span>
        <span class="secondary">Advisors, LLC</span>
      </h1>
    </div>

    <div class="phones">
      <p class="cell">C: 240.555.0143</p>
      <p class="fax">F: 240.555.0187</p>
    </div>

    <address class="address">
      5374 Tillbury Fenwood Road<br>
      Marrowfield<br>
      MD 20999
    </address>

    <p class="email">sales@verdantloopadvisors.example</p>
  </main>
</body>
</html>
```